existing Business Card Re design

We are wanting to re design our cards to reflect our new logo , i have attache the current business cards and new logo
i will need a business card that reflects the following information on each card.

card 1:
Gordon Thibeaux, President
555-182-4407
info@qlmcoatingpro.example

card 2:
Lionel Ostrander, Outside Sales
Office: 555-182-4407
Cell: 555-631-2958
Sales@qlmcoatingpro.example

Card 3
Tomas Varley, Branch Manager
Office: 555-182-4407
Cell: 555-274-8163
Tomas@qlmcoatingpro.example

Card 4
I will need a Generic card with no name on it just business
555-182-4407
info@qlmcoatingpro.example

Target Market(s)

Homeowners and Contractors

Contact Information for Business Card

We are wanting to re design our cards to reflect our new logo , i have attache the current business cards and new logo. same info on current card

card 1:
Gordon Thibeaux, President
555-182-4407
info@qlmcoatingpro.example

card 2:
Office: 555-182-4407
Cell: 555-631-2958
Sales@qlmcoatingpro.example

Card 3
Office: 555-182-4407
Cell: 555-274-8163
Tomas@qlmcoatingpro.example

Card 4
555-182-4407
info@qlmcoatingpro.example

Requirements
Must have
• same info as current cards with a added business
"sanitizing"

```html
<!DOCTYPE html>
<html lang="en">
<head>
<meta charset="utf-8">
<title>QLM Coating Pro – Business Cards</title>
<link href="https://fonts.googleapis.com/css2?family=Montserrat:wght@500;700;800;900&family=Poppins:wght@400;500;600&display=swap" rel="stylesheet">
<style>
  :root{
    --bg:#2b2623;
    --sky:#1fa0df;
    --blue:#1674c4;
    --navy:#0a1a3a;
    --ink:#05070d;
    --white:#ffffff;
    --paper:#ffffff;
  }
  *{box-sizing:border-box;margin:0;padding:0}
  html,body{width:1200px;height:780px;overflow:hidden;background:var(--bg)}
  body{font-family:"Poppins",sans-serif;color:var(--white)}

  .card-sheet{position:absolute;left:40px;top:60px;display:grid;grid-template-columns:540px 540px;grid-template-rows:300px 300px;gap:60px 40px}
  .card{position:relative;width:540px;height:300px;border-radius:18px;overflow:hidden}

  /* ---------- personal cards ---------- */
  .card-front{background:var(--paper)}
  .front-strip{position:absolute;left:0;top:0;width:34px;height:100%;background:var(--ink)}
  .front-strip .site{position:absolute;left:50%;top:50%;transform:translate(-50%,-50%) rotate(-90deg);
    white-space:nowrap;font-size:11px;font-weight:500;letter-spacing:.6px;text-transform:uppercase}
  .front-rule{position:absolute;left:34px;top:0;width:5px;height:100%;background:var(--sky)}
  .front-panel{position:absolute;left:39px;top:0;width:330px;height:100%;
    background:linear-gradient(180deg,var(--sky) 0%,var(--blue) 42%,var(--navy) 78%,var(--ink) 100%)}
  .person{position:absolute;left:34px;top:46px}
  .person .name{font-family:"Montserrat",sans-serif;font-weight:800;font-size:20px;letter-spacing:.8px;text-transform:uppercase;white-space:nowrap}
  .person .role{font-family:"Montserrat",sans-serif;font-weight:500;font-size:12.5px;letter-spacing:.6px;text-transform:uppercase;margin-top:2px}
  .contacts{position:absolute;left:34px;bottom:28px;list-style:none}
  .contacts li{display:flex;align-items:flex-start;gap:12px;font-size:13px;line-height:1.3;margin-top:4px;white-space:nowrap}
  .contacts li.address{margin-bottom:10px}
  .contacts svg{width:16px;height:16px;flex:none;margin-top:1px}
  .front-brand{position:absolute;left:369px;top:0;width:171px;height:100%;display:flex;align-items:center;justify-content:center}
  .front-brand .brand-name{transform:rotate(90deg);white-space:nowrap;font-family:"Montserrat",sans-serif;
    font-weight:900;font-size:27px;color:var(--blue);display:flex;align-items:center;gap:10px}
  .front-brand .brand-mark{width:14px;height:14px;background:var(--blue)}

  /* ---------- generic company card ---------- */
  .card-back{background:linear-gradient(180deg,var(--sky) 0%,var(--blue) 30%,var(--navy) 58%,var(--ink) 80%)}
  .back-brand{position:absolute;left:28px;top:58px;font-family:"Montserrat",sans-serif;font-weight:900;font-size:32px;line-height:1.08;color:var(--white)}
  .services{position:absolute;right:0;top:14px;list-style:none;width:240px}
  .services li{height:24px;margin-bottom:5px;border-radius:12px 0 0 12px;padding-left:24px;position:relative;
    background:linear-gradient(90deg,var(--sky) 0%,var(--blue) 35%,var(--navy) 100%);
    font-family:"Montserrat",sans-serif;font-weight:800;font-size:14px;line-height:24px;letter-spacing:.3px}
  .services li::before{content:"";position:absolute;left:11px;top:9px;width:6px;height:6px;border-radius:50%;background:var(--white)}
  .services li:nth-child(2){margin-left:8px}
  .services li:nth-child(3){margin-left:16px}
  .services li:nth-child(4){margin-left:24px}
  .services li:nth-child(5){margin-left:32px}
  .back-rule{position:absolute;left:0;right:0;height:1px;background:rgba(255,255,255,.75)}
  .back-rule.top{top:168px}
  .back-rule.bottom{top:240px}
  .back-phone{position:absolute;left:0;right:0;top:170px;text-align:center;font-family:"Montserrat",sans-serif;
    font-weight:800;font-size:56px;letter-spacing:1px;line-height:68px}
  .back-links{position:absolute;left:18px;right:18px;top:244px;display:flex;justify-content:space-between}
  .back-links span{display:flex;align-items:center;gap:8px;font-size:12px;white-space:nowrap}
  .back-links svg{width:16px;height:16px}
  .back-social{position:absolute;left:0;right:0;bottom:0;height:32px;background:linear-gradient(90deg,var(--sky),var(--blue) 60%,var(--navy));
    display:flex;align-items:center;gap:10px;padding-left:22px;font-size:14px}
  .back-social .dot{width:18px;height:18px;border-radius:50%;background:var(--white)}
</style>
</head>
<body>

<main class="card-sheet">

  <!-- Card 1 -->
  <section class="card card-front" aria-label="President business card">
    <div class="front-strip"><span class="site">www.qlmcoatingpro.example</span></div>
    <div class="front-rule"></div>
    <div class="front-panel">
      <div class="person">
        <p class="name">Gordon Thibeaux</p>
        <p class="role">President</p>
      </div>
      <ul class="contacts">
        <li class="address">
          <svg viewBox="0 0 16 16"><path d="M8 1a5 5 0 0 0-5 5c0 3.6 5 9 5 9s5-5.4 5-9a5 5 0 0 0-5-5z" fill="#fff"/><circle cx="8" cy="6" r="2" fill="#0a1a3a"/></svg>
          <span>4820 Larkspur Rd<br>Suite 12 Fairview, TX 75900</span>
        </li>
        <li>
          <svg viewBox="0 0 16 16"><circle cx="8" cy="8" r="8" fill="#fff"/><path d="M5 4.5l1.6-.4 1 2-1 .8a5 5 0 0 0 2.5 2.5l.8-1 2 1-.4 1.6c-3.8.3-6.8-2.7-6.5-6.5z" fill="#0a1a3a"/></svg>
          <span>555-182-4407</span>
        </li>
        <li>
          <svg viewBox="0 0 16 16"><circle cx="8" cy="8" r="8" fill="#fff"/><rect x="4" y="5" width="8" height="6" rx="1" fill="#0a1a3a"/><path d="M4.5 5.5L8 8.5l3.5-3" stroke="#fff" fill="none"/></svg>
          <span>info@qlmcoatingpro.example</span>
        </li>
      </ul>
    </div>
    <div class="front-brand"><span class="brand-name"><span class="brand-mark"></span>QLM Coating Pro</span></div>
  </section>

  <!-- Card 2 -->
  <section class="card card-front" aria-label="Outside sales business card">
    <div class="front-strip"><span class="site">www.qlmcoatingpro.example</span></div>
    <div class="front-rule"></div>
    <div class="front-panel">
      <div class="person">
        <p class="name">Lionel Ostrander</p>
        <p class="role">Outside Sales</p>
      </div>
      <ul class="contacts">
        <li class="address">
          <svg viewBox="0 0 16 16"><path d="M8 1a5 5 0 0 0-5 5c0 3.6 5 9 5 9s5-5.4 5-9a5 5 0 0 0-5-5z" fill="#fff"/><circle cx="8" cy="6" r="2" fill="#0a1a3a"/></svg>
          <span>4820 Larkspur Rd<br>Suite 12 Fairview, TX 75900</span>
        </li>
        <li>
          <svg viewBox="0 0 16 16"><circle cx="8" cy="8" r="8" fill="#fff"/><path d="M5 4.5l1.6-.4 1 2-1 .8a5 5 0 0 0 2.5 2.5l.8-1 2 1-.4 1.6c-3.8.3-6.8-2.7-6.5-6.5z" fill="#0a1a3a"/></svg>
          <span>Office: 555-182-4407</span>
        </li>
        <li>
          <svg viewBox="0 0 16 16"><circle cx="8" cy="8" r="8" fill="#fff"/><rect x="5.5" y="3.5" width="5" height="9" rx="1" fill="#0a1a3a"/><rect x="6.5" y="5" width="3" height="5" fill="#fff"/></svg>
          <span>Cell: 555-631-2958</span>
        </li>
        <li>
          <svg viewBox="0 0 16 16"><circle cx="8" cy="8" r="8" fill="#fff"/><rect x="4" y="5" width="8" height="6" rx="1" fill="#0a1a3a"/><path d="M4.5 5.5L8 8.5l3.5-3" stroke="#fff" fill="none"/></svg>
          <span>Sales@qlmcoatingpro.example</span>
        </li>
      </ul>
    </div>
    <div class="front-brand"><span class="brand-name"><span class="brand-mark"></span>QLM Coating Pro</span></div>
  </section>

  <!-- Card 3 -->
  <section class="card card-front" aria-label="Branch manager business card">
    <div class="front-strip"><span class="site">www.qlmcoatingpro.example</span></div>
    <div class="front-rule"></div>
    <div class="front-panel">
      <div class="person">
        <p class="name">Tomas Varley</p>
        <p class="role">Branch Manager</p>
      </div>
      <ul class="contacts">
        <li class="address">
          <svg viewBox="0 0 16 16"><path d="M8 1a5 5 0 0 0-5 5c0 3.6 5 9 5 9s5-5.4 5-9a5 5 0 0 0-5-5z" fill="#fff"/><circle cx="8" cy="6" r="2" fill="#0a1a3a"/></svg>
          <span>4820 Larkspur Rd<br>Suite 12 Fairview, TX 75900</span>
        </li>
        <li>
          <svg viewBox="0 0 16 16"><circle cx="8" cy="8" r="8" fill="#fff"/><path d="M5 4.5l1.6-.4 1 2-1 .8a5 5 0 0 0 2.5 2.5l.8-1 2 1-.4 1.6c-3.8.3-6.8-2.7-6.5-6.5z" fill="#0a1a3a"/></svg>
          <span>Office: 555-182-4407</span>
        </li>
        <li>
          <svg viewBox="0 0 16 16"><circle cx="8" cy="8" r="8" fill="#fff"/><rect x="5.5" y="3.5" width="5" height="9" rx="1" fill="#0a1a3a"/><rect x="6.5" y="5" width="3" height="5" fill="#fff"/></svg>
          <span>Cell: 555-274-8163</span>
        </li>
        <li>
          <svg viewBox="0 0 16 16"><circle cx="8" cy="8" r="8" fill="#fff"/><rect x="4" y="5" width="8" height="6" rx="1" fill="#0a1a3a"/><path d="M4.5 5.5L8 8.5l3.5-3" stroke="#fff" fill="none"/></svg>
          <span>Tomas@qlmcoatingpro.example</span>
        </li>
      </ul>
    </div>
    <div class="front-brand"><span class="brand-name"><span class="brand-mark"></span>QLM Coating Pro</span></div>
  </section>

  <!-- Card 4: generic -->
  <section class="card card-back" aria-label="Generic company business card">
    <p class="back-brand">QLM<br>Coating Pro</p>
    <ul class="services">
      <li>SPRAY FOAM</li>
      <li>FIBERGLASS</li>
      <li>INSULATION</li>
      <li>ROOFING</li>
      <li>SANITIZING</li>
    </ul>
    <div class="back-rule top"></div>
    <p class="back-phone">555-182-4407</p>
    <div class="back-rule bottom"></div>
    <div class="back-links">
      <span>
        <svg viewBox="0 0 16 16"><rect x="1.5" y="3.5" width="13" height="9" rx="1.2" fill="none" stroke="#fff" stroke-width="1.3"/><path d="M2 4l6 5 6-5" stroke="#fff" fill="none" stroke-width="1.2"/></svg>
        info@qlmcoatingpro.example
      </span>
      <span>
        <svg viewBox="0 0 16 16"><circle cx="8" cy="8" r="7" fill="none" stroke="#fff" stroke-width="1.3"/><ellipse cx="8" cy="8" rx="3" ry="7" fill="none" stroke="#fff"/><path d="M1 8h14M2.5 4.5h11M2.5 11.5h11" stroke="#fff"/></svg>
        www.qlmcoatingpro.example
      </span>
    </div>
    <div class="back-social"><span class="dot"></span><span>qlmcoatingpro</span></div>
  </section>

</main>

</body>
</html>
```